Can you create a Business Card based on the Logo you designed.

See example and would like to see other examples.

Trying to keep it very clean with a focus on the logo and name.

```html
<!DOCTYPE html>
<html lang="en">
<head>
<meta charset="utf-8">
<title>Growlia Business Card</title>
<link href="https://fonts.googleapis.com/css2?family=Montserrat:wght@600;700&family=Roboto:wght@400;500&display=swap" rel="stylesheet">
<style>
  :root {
    --stage: #e9e7e3;
    --orange: #e39131;
    --green: #1f7a3a;
    --leaf: #6cc24a;
    --paper: #f6f6f4;
    --ink: #222222;
    --accent: #e38a2a;
  }
  * { margin: 0; padding: 0; box-sizing: border-box; }
  html, body { width: 1200px; height: 779px; overflow: hidden; }
  body {
    background: var(--stage);
    position: relative;
    font-family: "Roboto", Arial, sans-serif;
  }
  .card {
    position: absolute;
    border-radius: 22px;
    box-shadow: 0 12px 30px rgba(0,0,0,0.18);
  }
  .card-front {
    left: 80px; top: 240px;
    width: 560px; height: 320px;
    background: var(--orange);
    display: flex; align-items: center; justify-content: center;
  }
  .card-back {
    left: 720px; top: 100px;
    width: 330px; height: 578px;
    background: var(--paper);
    border-bottom: 5px solid var(--leaf);
    padding: 60px 36px 50px;
    display: flex; flex-direction: column; align-items: center;
  }
  .brand {
    display: flex; align-items: center; gap: 12px;
    font-family: "Montserrat", Arial, sans-serif;
    font-weight: 700;
    color: var(--green);
    letter-spacing: 1px;
  }
  .brand-dot {
    border-radius: 50%;
    background: var(--paper);
  }
  .card-front .brand { font-size: 68px; }
  .card-front .brand-dot { width: 34px; height: 34px; }
  .card-back .brand { font-size: 44px; }
  .card-back .brand-dot { width: 22px; height: 22px; background: var(--accent); }
  .person { margin-top: 62px; text-align: center; }
  .person-name {
    font-family: "Montserrat", Arial, sans-serif;
    font-weight: 700; font-size: 26px; color: var(--green);
  }
  .person-title {
    margin-top: 6px; font-size: 18px; color: var(--accent);
  }
  .divider {
    width: 56px; height: 1.5px; background: var(--ink);
    margin: 46px 0 44px;
  }
  .contact { list-style: none; }
  .contact li {
    display: flex; align-items: center; gap: 10px;
    font-size: 19px; color: var(--ink); line-height: 1.6;
  }
  .contact svg { width: 16px; height: 16px; flex: none; }
</style>
</head>
<body>
  <section class="card card-front">
    <div class="brand"><span class="brand-dot"></span>Growlia</div>
  </section>

  <section class="card card-back">
    <div class="brand"><span class="brand-dot"></span>Growlia</div>
    <div class="person">
      <p class="person-name">Marcus Elling</p>
      <p class="person-title">Chief Executive officer</p>
    </div>
    <div class="divider"></div>
    <ul class="contact">
      <li>
        <svg viewBox="0 0 16 16"><path fill="#1f7a3a" d="M4 1.5l2.2 2.7-1.3 1.6c.9 2 2.3 3.4 4.3 4.3l1.6-1.3 2.7 2.2-1.6 2.5C6.6 13.4 2.6 9.4 1.5 3.1z"/></svg>
        +1 (555) 014-2876
      </li>
      <li>
        <svg viewBox="0 0 16 16"><rect x="1" y="3" width="14" height="10" rx="1" fill="#1f7a3a"/><path d="M1.5 4l6.5 5 6.5-5" stroke="#fff" stroke-width="1.4" fill="none"/></svg>
        ceo@growlia.com
      </li>
      <li>
        <svg viewBox="0 0 16 16"><circle cx="8" cy="8" r="7" fill="#1f7a3a"/><path d="M1 8h14M8 1c-3 3.5-3 10.5 0 14M8 1c3 3.5 3 10.5 0 14" stroke="#fff" stroke-width="1" fill="none"/></svg>
        www.growlia.com
      </li>
    </ul>
  </section>
</body>
</html>
```